Webdesign für Sexualpädagogik
Zielgruppe
- Sexualpädagogik, Beratung und Sexualtherapie
- Vorträge und Seminare für Unternehmen / Institutionen Vorträge Sexualität in der Pflege / im Alter / Grenzen wahrnehmen
- Wechseljahreberatung, Beratung in der Lebensmitte
- ZIelgruppe: Menschen, die sich weiternetwickeln möchten, die Problme mit ihrer Sexualität haben, Paare, Jugendliche
letztes Interview in der Zeitung: https://www.4927.ch/talbotenblatt/archiv/gespraech-im-fokus/beratung-endet-nicht-an-der-tuer-zur-klinik-hin/
Aufgabenstellung
- bestehende Internetseite siehe unten: Schrift ist Especial Key von Klarer Bogen
- auf dem Briefpapier bisher noch der Fachbuchhandel und Onlinhandel, aber beides nicht mehr
- Bilder zum Thema bereist vorhanden
- für Werbeflyer habe ich die Therapie in dunkelblau gehalten udn in der sexualpädagogik in hellblau
der wunderkiste wird aus der website entfernet

```html
<!DOCTYPE html>
<html lang="de">
<head>
<meta charset="utf-8">
<title>Klarer Bogen – Sexualpädagogik, Beratung und Therapie</title>
<link rel="stylesheet" href="https://fonts.googleapis.com/css2?family=Roboto:ital,wght@0,300;0,400;0,500;0,700;1,400;1,500&display=swap">
<style>
:root{
  --brand:#0a4aa8;
  --nav-active:#0d1f8c;
  --deep:#0647a6;
  --band:#1b5fb8;
  --light:#b8dafc;
  --ink:#333;
  --muted:#666;
  --paper:#fff;
  --grey:#f5f5f5;
  --line:#e2e2e2;
}
*{margin:0;padding:0;box-sizing:border-box}
html,body{width:1200px;height:2475px;overflow:hidden}
body{position:relative;background:var(--paper);font-family:"Roboto",sans-serif;color:var(--ink)}
.abs{position:absolute}

.hero{left:0;top:0;width:1200px;height:535px;background:linear-gradient(100deg,#eef2f8 0%,#dfe6f0 35%,#e9d9c9 60%,#cfdcf0 80%,#b7c9e6 100%)}
.brand{left:520px;top:18px;width:300px;text-align:center}
.brand-name{font-size:34px;font-weight:500;color:var(--brand);letter-spacing:2px;line-height:40px}
.brand-sub{font-size:12px;font-weight:400;color:#111;line-height:16px}
.brand-mark{left:400px;top:22px;width:62px;height:62px;border-radius:50%;background:var(--brand)}
.top-phone{left:935px;top:14px;font-size:12px;color:rgba(255,255,255,.75)}

.nav{left:150px;top:114px;width:900px;height:47px;display:flex;background:var(--paper);border:1px solid #ddd}
.nav a{display:flex;align-items:center;justify-content:center;font-size:13.5px;color:#222;text-decoration:none;border-left:1px solid #ddd}
.nav a:first-child{border-left:none;background:var(--nav-active);color:#fff}

.hero-title{left:150px;top:262px;font-size:42px;font-weight:300;color:var(--brand);line-height:69px}
.hero-rule{left:152px;top:395px;width:35px;height:2px;background:var(--brand)}

.sec-title{width:1200px;left:0;text-align:center;font-size:25px;font-weight:400}
.sec-title::after{content:"";display:block;width:76px;height:2px;margin:2px auto 0;background:currentColor;opacity:.6}
.who-title{top:576px;color:var(--brand)}
.who-text{left:151px;top:659px;width:394px;font-size:14px;font-weight:300;line-height:22.5px;text-align:justify;color:#222}
.who-text p+p{margin-top:22.5px}
.who-photo{left:587px;top:662px;width:423px;height:252px;background:linear-gradient(135deg,#e9e3dc 0%,#cfa88e 45%,#2b3a5c 80%,#1f2a44 100%)}

.services{left:0;top:975px;width:1200px;height:412px;background:linear-gradient(160deg,#1d5fb9 0%,#1756b1 50%,#2a6cc0 100%)}
.services-title{top:1032px;color:#fff}
.card{top:1103px;width:270px;height:206px;background:var(--paper);text-align:center}
.card .icon{width:110px;height:110px;margin:24px auto 0;border-radius:8px;background:linear-gradient(#dbe6f6,#bcd0ee)}
.card .label{margin-top:32px;font-size:17px;color:#333}

.panel-dark{left:151px;top:1453px;width:440px;height:254px;background:var(--deep);color:#fff;text-align:center}
.panel-light{left:566px;top:1485px;width:483px;height:254px;background:var(--light);text-align:center}
.panel h3{font-size:27px;font-weight:400;margin-top:34px}
.panel p{font-size:14px;line-height:21px;text-align:left}
.panel-dark p{margin:19px 22px 0 32px}
.panel-light h3{color:#111}
.panel-light p{margin:19px 50px 0 49px;color:#333;font-weight:300}
.btn{display:inline-block;font-size:13.5px;padding:5px 9px}
.panel-dark .btn{background:#fff;color:var(--brand);margin-top:20px}
.panel-light .btn{background:var(--deep);color:#fff;margin-top:28px}
.panel-art-a{left:151px;top:1603px;width:62px;height:104px;background:linear-gradient(#2a63b8,#3f78c6)}
.panel-art-b{left:882px;top:1647px;width:146px;height:76px;background:linear-gradient(90deg,#8fbdf0,#9cc6f4)}

.quote-band{left:0;top:1792px;width:1200px;height:245px;background:var(--grey);border-top:1px solid var(--line);border-bottom:1px solid var(--line)}
.quote-photo{left:238px;top:1838px;width:152px;height:152px;border-radius:50%;background:radial-gradient(circle at 50% 45%,#e8c6ad,#a0765a 70%,#6b4e3c)}
.quote-mark{left:368px;top:1846px;font-size:88px;line-height:88px;font-weight:700;color:var(--brand)}
.stars{left:445px;top:1838px;font-size:14px;letter-spacing:3px;color:var(--brand)}
.q-name{left:445px;top:1868px;font-size:13px;letter-spacing:2px;font-weight:500;color:#888}
.q-text{left:445px;top:1893px;width:550px;font-size:12px;line-height:17.5px;color:#666}
.q-rule{left:445px;top:1981px;width:22px;height:2px;background:var(--brand)}
.arrow{font-size:22px;color:#222}

.news-title,.sem-title{top:2078px;font-size:24px;color:var(--brand)}
.news-title{left:153px}
.sem-title{left:700px}
.news-item{left:154px;width:460px;font-size:12.5px;line-height:17.5px;color:#333;font-weight:300}
.news-item b{font-weight:500;color:#111}
.sem-box{left:701px;top:2124px;width:348px;height:177px;background:var(--deep);color:#fff;padding:30px 0 0 39px;font-size:17px;line-height:26px}

.footer{left:0;top:2350px;width:1200px;height:54px;background:var(--deep)}
.footer-links{left:150px;top:2370px;font-size:12.5px;color:#fff;display:flex;gap:24px}
.footer-legal{left:855px;top:2370px;font-size:12.5px;font-weight:500;color:#fff}
.social{top:2428px;font-size:12px;color:var(--brand);font-weight:500}
</style>
</head>
<body>

<div class="abs hero" role="img" aria-label="Porträt einer lächelnden Frau in hellblauem Pullover vor hellem Hintergrund"></div>
<div class="abs brand-mark" aria-hidden="true"></div>
<div class="abs brand">
  <div class="brand-name">KLARER BOGEN</div>
  <div class="brand-sub">Fachstelle für Sexualpädagogik, Beratung und Therapie<br>Mara Vollenweider</div>
</div>
<div class="abs top-phone">✉ 123 456 7890</div>

<nav class="abs nav">
  <a style="width:136px">HOME</a>
  <a style="width:156px">ÜBER MICH</a>
  <a style="width:158px">GÄSTEBUCH</a>
  <a style="width:165px">NEWSLETTER</a>
  <a style="width:121px">PREISE</a>
  <a style="width:164px">KONTAKT</a>
</nav>

<h1 class="abs hero-title">Sexualpädagogik,<br>Beratung und Sexualtherapie</h1>
<div class="abs hero-rule"></div>

<h2 class="abs sec-title who-title">WER WIR SIND</h2>
<div class="abs who-text">
  <p>Lorem ipsum dolor sit amet, consectetuer adipiscing elit. Class aptent taciti sociosqu ad litora torquent per conubia nostra, per inceptos hymenaeos. Nulla non arcu lacinia neque faucibus fringilla. Ut enim ad minim veniam, quis nostrud exercitation ullamco laboris nisi ut aliquip ex ea commodo consequat. Nam quis nulla. Ut tempus purus at lorem.</p>
  <p>Duis aute irure dolor in reprehenderit in voluptate velit esse cillum dolore eu fugiat nulla pariatur. Fusce wisi. Nullam lectus justo, vulputate eget mollis sed, tempor sed magna.</p>
</div>
<div class="abs who-photo" role="img" aria-label="Foto einer Rückenbehandlung mit Händen auf dem Rücken einer liegenden Person"></div>

<section class="abs services"></section>
<h2 class="abs sec-title services-title">WAS WIR TUN</h2>
<div class="abs card" style="left:150px"><div class="icon" role="img" aria-label="Illustration: Kopf mit Geschlechtersymbolen"></div><div class="label">Sexualpädagogik</div></div>
<div class="abs card" style="left:463px"><div class="icon" role="img" aria-label="Illustration: zwei Gesichter im Profil"></div><div class="label">Sexualberatung / Sexualtherapie</div></div>
<div class="abs card" style="left:780px"><div class="icon" role="img" aria-label="Illustration: zwei Personen im Gespräch am Tisch"></div><div class="label">Wechseljahrberatung</div></div>

<div class="abs panel panel-dark">
  <h3>Therapie</h3>
  <p>Lorem ipsum dolor sit amet, consectetuer adipiscing elit. Class aptent taciti sociosqu ad litora torquent per conubia nostra, per inceptos hymenaeos.</p>
  <span class="btn">Weiterlesen</span>
</div>
<div class="abs panel-art-a" role="img" aria-label="Illustration: Frauenfigur mit Wirbelsäule"></div>
<div class="abs panel panel-light">
  <h3>Sexualpädagogik</h3>
  <p>Sex education is the educational work with girls and boys on their questions about love, feelings and sexuality as well as gender aspects.</p>
  <span class="btn">Weiterlesen</span>
</div>
<div class="abs panel-art-b" role="img" aria-label="Illustration: Geschlechtersymbole"></div>

<section class="abs quote-band"></section>
<div class="abs arrow" style="left:180px;top:1904px">‹</div>
<div class="abs arrow" style="left:1008px;top:1904px">›</div>
<div class="abs quote-photo" role="img" aria-label="Porträtfoto einer jungen Frau mit langen Haaren"></div>
<div class="abs quote-mark">“</div>
<div class="abs stars">★★★★★</div>
<div class="abs q-name">JONAS WETTERLI</div>
<div class="abs q-text">Lorem ipsum dolor sit amet, consectetuer adipiscing elit. Class aptent taciti sociosqu ad litora torquent per conubia nostra, per inceptos hymenaeos. Nulla non arcu lacinia neque faucibus fringilla. Ut enim ad minim veniam, quis nostrud exercitation ullamco laboris nisi ut aliquip ex ea commodo consequat. Nam quis nulla. Ut tempus purus at lorem.</div>
<div class="abs q-rule"></div>

<h2 class="abs news-title" style="font-weight:400">News</h2>
<div class="abs arrow" style="left:577px;top:2078px;font-size:20px">‹</div>
<div class="abs arrow" style="left:599px;top:2078px;font-size:20px;color:var(--brand)">›</div>
<div class="abs news-item" style="top:2125px"><b>"I make everyone a good li ...</b><br>Brig-Glis / Where others blush, she speaks plain text. Mara Vollenweider is a sex pedagogue and says: "Sex is learnable." - - By Lea Morand - Nina Brunner - - Which one is ... [more]</div>
<div class="abs news-item" style="top:2218px"><b>"Mail's to info@klarer-bogen.ch</b><br>Unfortunately in the last week many mails of love learning were devoured by the spam filter. - - I apologize for the inconvenience. Maybe just ... [more]</div>

<h2 class="abs sem-title" style="font-weight:400">Nächste Seminare</h2>
<div class="abs sem-box">xxxxxxxxxxxxxxxxxxxxxxxx<br>xxxxxxxxxxxxxxx<br>xxxxxxxxxxxxxxxxxxxx<br>Daten: Nov, 13, 2018<br>Ruf uns jetzt an: 123-456-7890</div>

<footer class="abs footer"></footer>
<div class="abs footer-links"><span>Impressum</span><span>Lageplan</span><span>News</span><span>Nächste Seminare</span><span>Kontakt</span><span>über Mara Vollenweider / Klarer Bogen</span></div>
<div class="abs footer-legal">Datenschutz | Terms &amp; Bedingungen</div>
<div class="abs social" style="left:930px">Kontaktnetz</div>
<div class="abs social" style="left:1005px">Freundeskreis</div>

</body>
</html>
```